Online Marketplace Startup for Community Facilities (Tovaroom)

A innovative, modern website design is required for a new startup called Tovaroom. Tovaroom will be an online marketplace for searching for and booking community facilities, such as schools facilities (sports grounds, halls, classrooms etc.), churches, hospitals and other community facilities.

The attached brief has been created to provide guidance on the structure and content required.

The web design shall feature a modern, innovative but user friendly interface similar style to other web start up pages:
www.hallquiver.co.uk
www.vendlark.com.au
www.artfennel.com.au

The web design shall be ‘wordpress’ compliant and allow for future functionality to be added and coded (e.g. animations, flash, blogs etc) and content to be editable.

The following brief has been created to provide guidance on the structure and content required.

An existing logo developed for Tovaroom shall be utilised and incorporated in the top left hand cover of the cover landing page (refer to attached logo designs).

Refer to attached 'Website brief' for more details on requirements.
Updates

Project Deadline Extended
Reason: I wish to grant an extension to the deadline to provide designers with more time to submit their designs.

Target Market(s)

TovaRoom will focus on building a customer network of both community facility owners (schools, hospitals, churches) and hirers (non-government organisations, community groups, event management companies, commercial businesses). Members of the general public will also be encouraged to book facilities for private functions.

Industry/Entity Type

Community

Coding

Coded - Design and coding required

Number of Pages Required

5+ page

Font styles to use
Sans Serif

Colors
3176b5
ffffff
85cae6
33a6d7

Requirements
Must have
• The web design shall feature a modern, innovative but user friendly interface similar style to other web start up pages:
• www.hallquiver.co.uk
• www.vendlark.com.au
• www.artfennel.com.au
• The web design shall be ‘wordpress’ compliant and allow for future functionality to be added and coded (e.g. animations, flash, blogs etc) and content to be editable.
• Refer to Project brief for other requirements
Nice to have
• Refer to Project brief
Should not have
• Refer to Project brief

```html
<!DOCTYPE html>
<html lang="en">
<head>
<meta charset="utf-8">
<title>TovaRoom — Utilising Your Facility</title>
<link href="https://fonts.googleapis.com/css2?family=Montserrat:wght@400;600;700;800&family=Work+Sans:wght@300;400;500&display=swap" rel="stylesheet">
<style>
:root{
  --blue:#2d63bf;
  --blue-deep:#1f4ea6;
  --navy:#1c3a6e;
  --yellow:#f3cd0d;
  --ink:#1d2f55;
  --text:#6f7480;
  --muted:#9a9ea6;
  --grey-bg:#f4f5f7;
  --line:#d9dbe0;
  --white:#ffffff;
}
*{margin:0;padding:0;box-sizing:border-box}
html,body{width:1200px;height:4119px;overflow:hidden}
body{position:relative;background:var(--white);font-family:"Work Sans",Arial,sans-serif;color:var(--text)}
.abs{position:absolute}
.head{font-family:"Montserrat",Arial,sans-serif;color:var(--ink);font-weight:700;text-transform:uppercase;text-align:center;font-size:34px;letter-spacing:.5px}
.rule{width:80px;height:4px;background:var(--yellow);margin:14px auto 0}
.btn{display:inline-block;font-family:"Montserrat",Arial,sans-serif;font-weight:700;font-size:15px;text-transform:uppercase;letter-spacing:1px;border:3px solid var(--yellow);padding:10px 20px;text-decoration:none}

/* hero */
.hero{left:0;top:0;width:1200px;height:600px;background:linear-gradient(180deg,var(--blue) 0%,var(--blue-deep) 100%)}
.topbar{left:225px;top:32px;width:750px;height:26px;font-size:12px;color:#dfe7f7;font-family:"Montserrat",Arial,sans-serif}
.topbar .contact-info{position:absolute;left:0;top:6px;display:flex;gap:18px;align-items:center}
.topbar .logo{position:absolute;left:50%;transform:translateX(-50%);top:0;display:flex;align-items:center;gap:10px;color:#fff;font-size:28px;font-weight:600;letter-spacing:.3px;text-transform:none}
.topbar .logo i{display:block;width:22px;height:22px;background:#fff}
.topbar .util{position:absolute;right:0;top:6px;display:flex;gap:16px;font-size:11px;text-transform:uppercase}
.topbar .util b{color:#fff}
.topline{left:225px;top:84px;width:750px;height:1px;background:rgba(255,255,255,.35)}
.nav{left:225px;top:114px;display:flex;gap:40px;font-family:"Montserrat",Arial,sans-serif;font-size:13px;text-transform:uppercase;color:#dfe7f7;letter-spacing:.5px}
.nav .active{color:#fff;font-weight:700;position:relative}
.nav .active::before{content:"";position:absolute;left:0;top:-32px;width:100%;height:4px;background:var(--yellow)}
.burger{left:945px;top:110px;width:30px;height:20px;border-top:3px solid var(--yellow);border-bottom:3px solid var(--yellow)}
.burger::after{content:"";position:absolute;left:0;top:5px;width:30px;height:3px;background:var(--yellow)}
.hero-title{left:0;top:172px;width:1200px;text-align:center;font-family:"Montserrat",Arial,sans-serif;font-weight:800;font-size:52px;color:#fff;letter-spacing:1px}
.hero-sub{left:0;top:246px;width:1200px;text-align:center;font-size:19px;color:#dbe5f7;font-weight:300}
.hero-cta{left:494px;top:298px;width:212px;text-align:center;color:var(--yellow);background:transparent}
.hero-wave{left:0;top:480px}
.laptop{left:431px;top:385px}

/* services */
.services{left:0;top:560px;width:1200px;height:626px;background:var(--grey-bg)}
.services-title{left:0;top:680px;width:1200px}
.services-desc{left:225px;top:762px;width:750px;text-align:center;font-size:15px;line-height:24px;color:var(--muted)}
.service-grid{left:225px;top:873px;width:750px;height:247px;display:grid;grid-template-columns:repeat(3,1fr);grid-template-rows:repeat(2,1fr)}
.service{display:flex;flex-direction:column;align-items:center;justify-content:flex-end;padding-bottom:18px;gap:12px;font-family:"Montserrat",Arial,sans-serif;font-weight:600;font-size:15px;color:var(--ink);text-transform:uppercase;border-bottom:1px solid var(--line)}
.service.mid{border-left:1px solid var(--line);border-right:1px solid var(--line)}
.service.top{border-bottom:1px solid var(--ink)}
.service.featured{background:var(--navy);color:#fff;justify-content:center;gap:8px;padding:0}
.service.featured small{font-family:"Work Sans",Arial,sans-serif;font-size:10px;text-transform:none;font-weight:400;color:#c8d2e6}
.service.featured span.book{background:var(--yellow);color:var(--ink);font-size:10px;padding:5px 14px;font-weight:700}

/* about */
.about-title{left:225px;top:1300px;font-size:34px;text-align:left}
.about-title .rule{margin:12px 0 0}
.about-text{left:225px;top:1385px;width:370px;font-size:15px;line-height:23px;color:var(--muted)}
.about-btn{left:225px;top:1510px;color:var(--ink);font-size:14px;padding:10px 16px}
.about-frame{left:722px;top:1296px;width:252px;height:228px;border:7px solid var(--yellow)}
.about-photo{left:642px;top:1327px;width:309px;height:220px;background:linear-gradient(135deg,#c9d9de,#7e9ba3 60%,#46626c);box-shadow:0 10px 24px rgba(0,0,0,.18)}

/* team */
.team-title{left:0;top:1705px;width:1200px}
.member-frame{width:226px;height:190px;border:7px solid var(--yellow)}
.member-frame.grey{border-color:#9a9ea6}
.member-photo{width:228px;height:228px}
.member-info{width:260px;text-align:center;font-size:14px;color:var(--muted);line-height:24px}
.member-info h3{font-family:"Montserrat",Arial,sans-serif;font-size:16px;color:var(--ink);font-weight:700;margin-bottom:6px;letter-spacing:.5px}
.member-info.grey h3{color:#9a9ea6}
.member-info .bio{margin-top:10px;background:var(--yellow);border-color:var(--yellow);color:var(--ink);font-size:13px;padding:8px 28px}
.member-info.grey .bio{background:transparent;border-color:#b9bcc2;color:#9a9ea6}
.arrow-btn{width:44px;height:44px}

/* cta band */
.band{left:0;top:2340px;width:1200px;height:252px;background:var(--navy);text-align:center;color:#fff}
.band h2{font-family:"Montserrat",Arial,sans-serif;font-weight:800;font-size:32px;margin-top:52px;letter-spacing:.5px}
.band p{font-size:18px;line-height:28px;color:#d7dfee;margin:14px auto 0;width:520px}
.band .btn{margin-top:18px;color:var(--yellow);font-size:14px;padding:8px 22px}

/* clients */
.clients-title{left:0;top:2685px;width:1200px}
.client{display:flex;align-items:center;gap:10px;font-family:"Montserrat",Arial,sans-serif;font-weight:700;font-size:34px;letter-spacing:1px}
.client.faint{color:#c6c8cd}
.client-card{left:478px;top:2810px;width:228px;height:160px;background:#fff;box-shadow:0 8px 22px rgba(0,0,0,.15);justify-content:center;color:#222}
.client-frame{left:558px;top:2782px;width:166px;height:140px;border:7px solid var(--yellow)}
.dots{left:545px;top:3026px;display:flex;gap:15px}
.dots i{width:14px;height:14px;border-radius:50%;background:#d7d9dd}
.dots i.on{background:var(--yellow)}

/* news */
.news{left:0;top:3117px;width:1200px;height:700px;background:var(--grey-bg)}
.news-title{left:0;top:3210px;width:1200px}
.news-card{top:3323px;width:210px;height:384px;border:6px solid var(--yellow);background:#fff;padding:22px 18px}
.news-card h4{font-family:"Montserrat",Arial,sans-serif;font-weight:700;color:var(--ink);font-size:21px;line-height:28px}
.news-card .rule{margin:14px 0 14px;width:44px;height:3px}
.news-card p{font-size:13px;line-height:19px;color:var(--text)}
.news-card .more{display:block;margin-top:16px;font-family:"Montserrat",Arial,sans-serif;font-size:11px;font-weight:700;color:var(--ink)}
.news-feature{left:494px;top:3323px;width:212px;height:384px;background:#fff;box-shadow:0 8px 22px rgba(0,0,0,.14)}
.news-feature .img{height:192px;background:linear-gradient(180deg,#2b7fc8 0%,#6fb3e3 45%,#e9eef2 100%)}
.news-feature h4{font-family:"Montserrat",Arial,sans-serif;font-weight:700;color:var(--ink);font-size:22px;line-height:29px;padding:20px 28px 0}
.news-feature .btn{margin:10px 28px;padding:3px 10px;font-size:11px;border-width:3px;color:var(--yellow);text-transform:none;letter-spacing:0}
.up-arrow{left:584px;top:3760px}

/* footer */
.footer{left:0;top:3817px;width:1200px;height:302px;background:var(--navy);color:#fff}
.footer-nav{position:absolute;left:0;top:80px;width:1200px;display:flex;justify-content:center;gap:40px;font-family:"Montserrat",Arial,sans-serif;font-size:12px;text-transform:uppercase;color:#c8d2e6}
.footer-nav b{color:#fff}
.subscribe{position:absolute;left:423px;top:123px;width:352px;height:45px;display:flex}
.subscribe .field{flex:1;background:#fff;color:#777;font-size:13px;padding:14px 16px}
.subscribe .go{width:120px;background:var(--yellow);color:var(--ink);font-family:"Montserrat",Arial,sans-serif;font-size:12px;font-weight:700;display:flex;align-items:center;justify-content:center;text-transform:uppercase}
.social{position:absolute;left:0;top:198px;width:1200px;display:flex;justify-content:center;gap:26px}
.social i{width:16px;height:16px;border-radius:50%;background:#fff;display:block}
.copy{position:absolute;left:0;top:248px;width:1200px;text-align:center;font-size:12px;color:#d7dfee}
</style>
</head>
<body>

<!-- hero -->
<div class="abs hero"></div>
<div class="abs topbar">
  <div class="contact-info">
    <svg width="12" height="12" viewBox="0 0 24 24"><path fill="#fff" d="M6.6 10.8a15 15 0 0 0 6.6 6.6l2.2-2.2c.3-.3.7-.4 1-.2 1.1.4 2.3.6 3.6.6.6 0 1 .4 1 1V20c0 .6-.4 1-1 1A17 17 0 0 1 3 4c0-.6.4-1 1-1h3.5c.6 0 1 .4 1 1 0 1.3.2 2.5.6 3.6.1.3 0 .7-.2 1z"/></svg>
    <span>040 555 0182</span>
    <svg width="11" height="13" viewBox="0 0 20 26"><path fill="#fff" d="M10 0a9 9 0 0 0-9 9c0 7 9 17 9 17s9-10 9-17a9 9 0 0 0-9-9zm0 12a3 3 0 1 1 0-6 3 3 0 0 1 0 6z"/></svg>
    <span>Larkfield East</span>
  </div>
  <div class="logo"><i></i>TovaRoom</div>
  <div class="util"><span>News</span><span>FAQ</span><b>Contact</b></div>
</div>
<div class="abs topline"></div>
<div class="abs nav">
  <span class="active">Home</span><span>About</span><span>How it works</span><span>Services</span><span>Packages</span><span>Why us?</span>
</div>
<div class="abs burger"></div>
<div class="abs hero-title">UTILISING YOUR FACILITY</div>
<div class="abs hero-sub">to create value for your organisation and the community</div>
<a class="abs btn hero-cta">Contact us</a>

<svg class="abs hero-wave" width="1200" height="130" viewBox="0 0 1200 130" aria-hidden="true">
  <path d="M0 60 Q600 150 1200 30 L1200 130 L0 130 Z" fill="#f4f5f7"/>
</svg>

<svg class="abs laptop" width="343" height="245" viewBox="0 0 343 245">
  <rect x="12" y="0" width="319" height="222" rx="10" fill="#1b1d22"/>
  <rect x="22" y="10" width="299" height="200" fill="#b9c3c9" role="img" aria-label="Photo of a team meeting around a conference table"/>
  <circle cx="171" cy="110" r="18" fill="#f3cd0d"/>
  <path d="M165 100 L181 110 L165 120 Z" fill="#fff"/>
  <path d="M0 222 H343 L335 238 Q333 245 325 245 H18 Q10 245 8 238 Z" fill="#c9ccd2"/>
  <rect x="145" y="222" width="53" height="5" rx="2" fill="#a6aab1"/>
</svg>

<!-- services -->
<div class="abs services"></div>
<div class="abs head services-title">Services we offer<div class="rule"></div></div>
<p class="abs services-desc">Although, today we're even more excited to release our Wireframe Kit. The name speaks for itself and how you could've already guessed, Wireframe Kit is a perfect.</p>
<div class="abs service-grid">
  <div class="service top">
    <svg width="48" height="48" viewBox="0 0 48 48"><ellipse cx="22" cy="30" rx="16" ry="12" fill="none" stroke="#1d2f55" stroke-width="2.5"/><circle cx="24" cy="12" r="6" fill="#f3cd0d" stroke="#1d2f55" stroke-width="2"/><rect x="12" y="40" width="5" height="6" fill="#1d2f55"/><rect x="27" y="40" width="5" height="6" fill="#1d2f55"/></svg>
    Savings
  </div>
  <div class="service mid featured">
    Financial News
    <small>1 hr introductory meeting</small>
    <span class="book">BOOK NOW &gt;</span>
  </div>
  <div class="service top">
    <svg width="52" height="48" viewBox="0 0 52 48"><rect x="6" y="18" width="40" height="26" fill="none" stroke="#1d2f55" stroke-width="2.5"/><rect x="14" y="4" width="24" height="14" fill="#f3cd0d" stroke="#1d2f55" stroke-width="2"/><line x1="6" y1="30" x2="46" y2="30" stroke="#1d2f55" stroke-width="2"/></svg>
    Investments
  </div>
  <div class="service">
    <svg width="48" height="48" viewBox="0 0 48 48"><rect x="6" y="6" width="36" height="28" fill="#f3cd0d" stroke="#1d2f55" stroke-width="2.5"/><polyline points="12,26 20,18 27,23 36,12" fill="none" stroke="#1d2f55" stroke-width="2.5"/><line x1="16" y1="34" x2="10" y2="46" stroke="#1d2f55" stroke-width="2.5"/><line x1="32" y1="34" x2="38" y2="46" stroke="#1d2f55" stroke-width="2.5"/></svg>
    Business planning
  </div>
  <div class="service mid">
    <svg width="52" height="44" viewBox="0 0 52 44"><rect x="4" y="8" width="40" height="28" rx="3" fill="#f3cd0d" stroke="#1d2f55" stroke-width="2.5"/><rect x="4" y="15" width="40" height="6" fill="#1d2f55"/><rect x="10" y="27" width="12" height="4" fill="#1d2f55"/></svg>
    Credit card
  </div>
  <div class="service">
    <svg width="44" height="48" viewBox="0 0 44 48"><rect x="6" y="4" width="32" height="40" rx="3" fill="#f3cd0d" stroke="#1d2f55" stroke-width="2.5"/><rect x="11" y="9" width="22" height="9" fill="#fff" stroke="#1d2f55" stroke-width="2"/><g fill="#1d2f55"><rect x="11" y="23" width="5" height="5"/><rect x="20" y="23" width="5" height="5"/><rect x="29" y="23" width="5" height="5"/><rect x="11" y="32" width="5" height="5"/><rect x="20" y="32" width="5" height="5"/><rect x="29" y="32" width="5" height="5"/></g></svg>
    Interest
  </div>
</div>

<!-- about -->
<div class="abs head about-title">About us<div class="rule"></div></div>
<p class="abs about-text">TovaRoom is a start-up recently formed in 2017 in Melbourne, Australia by husband and wife co-founders Marlo Venski and Oda Prentiss.</p>
<a class="abs btn about-btn">Read more &gt;</a>
<div class="abs about-frame"></div>
<div class="abs about-photo" role="img" aria-label="Photo of a hand signing a document with a pen"></div>

<!-- team -->
<div class="abs head team-title">Our team<div class="rule"></div></div>
<svg class="abs arrow-btn" style="left:162px;top:1925px" viewBox="0 0 44 44"><circle cx="22" cy="22" r="19" fill="none" stroke="#9a9ea6" stroke-width="3"/><path d="M30 22H14M21 14l-8 8 8 8" fill="none" stroke="#9a9ea6" stroke-width="3"/></svg>
<svg class="abs arrow-btn" style="left:975px;top:1925px" viewBox="0 0 44 44"><circle cx="22" cy="22" r="19" fill="none" stroke="#f3cd0d" stroke-width="3"/><path d="M14 22h16M23 14l8 8-8 8" fill="none" stroke="#f3cd0d" stroke-width="3"/></svg>

<div class="abs member-frame" style="left:310px;top:1810px"></div>
<div class="abs member-photo" role="img" aria-label="Portrait photo of the company CEO" style="left:285px;top:1837px;background:linear-gradient(180deg,#d6d9de,#8b8f97)"></div>
<div class="abs member-info" style="left:269px;top:2088px">
  <h3>DARIO KEMBLE, CEO</h3>
  <div>✉ dario@quillmark.com</div>
  <div>☏ 555-014-2290</div>
  <a class="btn bio">View bio &gt;</a>
</div>

<div class="abs member-frame grey" style="left:670px;top:1810px"></div>
<div class="abs member-photo" role="img" aria-label="Portrait photo of the company CFO" style="left:645px;top:1837px;background:linear-gradient(180deg,#e4e5e7,#a9abaf)"></div>
<div class="abs member-info grey" style="left:629px;top:2088px">
  <h3>LENA ORSGAARD, CFO</h3>
  <div>✉ lena@quillmark.com</div>
  <div>☏ 555-014-2290</div>
  <a class="btn bio">View bio &gt;</a>
</div>

<!-- cta band -->
<div class="abs band">
  <h2>NEED MORE DETAILS?</h2>
  <p>We are here to assist. Contact us by phone, email or via our Social Media channels.</p>
  <a class="btn">Contact us</a>
</div>

<!-- clients -->
<div class="abs head clients-title">Our clients<div class="rule"></div></div>
<div class="abs client faint" style="left:230px;top:2870px;font-size:30px">MARROW&amp;CO</div>
<div class="abs client-frame"></div>
<div class="abs client client-card">STALWICK</div>
<div class="abs client faint" style="left:808px;top:2868px">ZENTRO</div>
<div class="abs dots"><i></i><i class="on"></i><i></i><i></i></div>

<!-- news -->
<div class="abs news"></div>
<div class="abs head news-title">Latest news<div class="rule"></div></div>
<div class="abs news-card" style="left:225px">
  <h4>Manage Your Blog from Your Live Site</h4>
  <div class="rule"></div>
  <p>Lorem ipsum dolor sit amet, fali mollis legendos at sit, vix ea nostrud quaeque explicari. Feugiat luptatum sea ea, omnis cetero id usu, no verterem volutpat.</p>
  <span class="more">Read More &gt;</span>
</div>
<div class="abs news-feature">
  <div class="img" role="img" aria-label="Photo of a white seaside village above a blue sea"></div>
  <h4>Design a Stunning Website</h4>
  <a class="btn">Open Blog Page</a>
</div>
<div class="abs news-card" style="left:769px">
  <h4>Manage Your Blog from Your Live Site</h4>
  <div class="rule"></div>
  <p>Lorem ipsum dolor sit amet, fali mollis legendos at sit, vix ea nostrud quaeque explicari. Feugiat luptatum sea ea, omnis cetero id usu, no verterem volutpat.</p>
  <span class="more">Read More &gt;</span>
</div>
<svg class="abs up-arrow" width="32" height="40" viewBox="0 0 32 40"><path d="M4 3H28M16 10V38M7 19l9-9 9 9" fill="none" stroke="#1d2f55" stroke-width="2"/></svg>

<!-- footer -->
<div class="abs footer">
  <div class="footer-nav"><b>Home</b><span>About</span><span>How it works</span><span>Services</span><span>Packages</span><span>Why us?</span></div>
  <div class="subscribe"><div class="field">Email Address</div><div class="go">Subscribe now</div></div>
  <div class="social"><i></i><i></i><i></i><i></i></div>
  <div class="copy">All Rights Reserved 2017 studio@pellworth.com</div>
</div>

</body>
</html>
```